Dog Coat Drive for San Francisco Homeless Pets

- one page, full color, flyer to advertise a winter dog coat drive.- requesting use of an image of pit bull type or chihuahua type dog in a coat - 2 size versions - 8.5 inch by 11 inch to be printed and a square design to be posted on FB, Instagram and websites

Font styles to use
Serif
Sans Serif

Colors

Designer to choose colors to be used in the design.

```html
<!DOCTYPE html>
<html lang="en">
<head>
<meta charset="utf-8">
<title>Dog Coat Drive</title>
<link rel="stylesheet" href="https://fonts.googleapis.com/css2?family=Baloo+2:wght@600;700;800&family=Montserrat:wght@500;600&display=swap">
<style>
  :root {
    --sky: #1ea3e2;
    --sky-deep: #0a8fd0;
    --ink: #3b3b3d;
    --ink-dark: #1d1d1f;
    --paper: #ffffff;
    --blanket: #c9ad9c;
    --haze: #eef0f3;
  }
  * { margin: 0; padding: 0; box-sizing: border-box; }
  html, body { width: 934px; height: 1200px; overflow: hidden; background: var(--paper); }
  .flyer {
    position: relative; width: 934px; height: 1200px; overflow: hidden;
    background: var(--paper); font-family: "Baloo 2", sans-serif; color: var(--ink);
  }
  .hero-photo {
    position: absolute; left: 0; top: 0; width: 934px; height: 660px;
    background:
      radial-gradient(ellipse 260px 300px at 560px 250px, #b89a87 0%, rgba(200,170,152,0.85) 45%, rgba(220,205,196,0) 100%),
      radial-gradient(ellipse 420px 220px at 640px 460px, rgba(200,176,162,0.9) 0%, rgba(226,214,206,0.6) 55%, rgba(240,240,242,0) 100%),
      linear-gradient(180deg, #f1f2f4 0%, #e7e9ec 60%, #eceef0 100%);
    -webkit-mask-image: linear-gradient(180deg, #000 70%, transparent 100%);
            mask-image: linear-gradient(180deg, #000 70%, transparent 100%);
  }
  .brand { position: absolute; left: 58px; top: 70px; display: flex; align-items: center; gap: 12px; }
  .brand-dot { width: 52px; height: 52px; border-radius: 50%; background: var(--sky); }
  .brand-name { font-weight: 700; font-size: 40px; line-height: 1; color: var(--sky); }
  .brand-tag { position: absolute; left: 176px; top: 127px; font-family: "Montserrat", sans-serif; font-weight: 600; font-size: 16px; color: var(--ink-dark); }
  .bubble { position: absolute; left: 80px; top: 190px; width: 300px; height: 300px; }
  .bubble-text {
    position: absolute; left: 92px; top: 262px; width: 272px; text-align: center;
    color: var(--paper); font-weight: 800; font-size: 52px; line-height: 0.92;
  }
  .title {
    position: absolute; left: 0; width: 934px; top: 512px; text-align: center;
    font-weight: 800; font-size: 72px; line-height: 1; color: var(--sky);
    text-shadow: 0 2px 6px rgba(255,255,255,0.8);
  }
  .subtitle {
    position: absolute; left: 0; width: 934px; top: 596px; text-align: center;
    font-weight: 700; font-size: 38px; line-height: 1; color: var(--ink);
  }
  .dates {
    position: absolute; left: 232px; top: 664px; width: 470px; height: 52px; border-radius: 26px;
    background: var(--sky); color: var(--paper); font-weight: 700; font-size: 23px;
    display: flex; align-items: center; justify-content: center; padding-top: 3px;
  }
  .appeal {
    position: absolute; left: 40px; width: 854px; top: 732px; text-align: center;
    font-weight: 700; font-size: 19.5px; line-height: 32px; color: var(--ink);
  }
  .partners-head {
    position: absolute; left: 66px; width: 812px; top: 820px;
    display: flex; align-items: center; gap: 16px;
    color: var(--sky); font-weight: 700; font-size: 20px; white-space: nowrap;
  }
  .partners-head::before, .partners-head::after { content: ""; flex: 1; height: 1.5px; background: var(--sky); }
  .partner { position: absolute; width: 300px; text-align: center; }
  .partner-badge { margin: 0 auto 12px; background: var(--sky); }
  .badge-round { width: 68px; height: 68px; border-radius: 50%; }
  .badge-wide { width: 180px; height: 44px; border-radius: 4px; }
  .badge-square { width: 72px; height: 72px; border-radius: 8px; }
  .partner-name { font-weight: 700; font-size: 18px; line-height: 22px; color: var(--sky); }
  .partner-line {
    display: flex; align-items: center; justify-content: center; gap: 6px;
    font-weight: 700; font-size: 15px; line-height: 21px; color: var(--ink);
  }
  .partner-line svg { width: 12px; height: 13px; fill: var(--sky); flex: none; }
</style>
</head>
<body>
<main class="flyer">
  <div class="hero-photo" role="img" aria-label="Photo of a small dog wrapped in a soft tan blanket on a white bed"></div>

  <header class="brand">
    <span class="brand-dot"></span>
    <span class="brand-name">WarmPaws Wagon</span>
  </header>
  <p class="brand-tag">Mobile Pet Care Team</p>

  <svg class="bubble" viewBox="0 0 300 300" aria-hidden="true">
    <path d="M160 12 a138 138 0 1 1 -40 270 L48 296 L82 250 A138 138 0 0 1 160 12 Z" fill="#7fc8ee"/>
    <circle cx="158" cy="150" r="136" fill="#1ea3e2"/>
  </svg>
  <p class="bubble-text">Baby,<br>It’s Cold<br>Outside!</p>

  <h1 class="title">Dog Coat Drive</h1>
  <h2 class="subtitle">for SF Haven Centers</h2>
  <p class="dates">From December through February</p>
  <p class="appeal">Please donate new &amp; gently used dog coats, sweaters and jackets for Haven<br>Center dogs whose owners are working to prevent and end their homelessness</p>

  <h3 class="partners-head">Coat drop partners and locations</h3>

  <section class="partner" style="left:10px; top:862px;">
    <div class="partner-badge badge-wide"></div>
    <p class="partner-name" style="margin-top:22px">Bay City Shelter</p>
    <p class="partner-line"><svg viewBox="0 0 12 14"><path d="M6 0a5 5 0 0 0-5 5c0 3.6 5 9 5 9s5-5.4 5-9a5 5 0 0 0-5-5zm0 7a2 2 0 1 1 0-4 2 2 0 0 1 0 4z"/></svg>1450 Alder Street</p>
    <p class="partner-line"><svg viewBox="0 0 14 14"><path d="M3 0l3 3-1.6 2a8 8 0 0 0 4.6 4.6L11 8l3 3-2 3C6 14 0 8 0 2z"/></svg>415-555-0141</p>
  </section>

  <section class="partner" style="left:303px; top:862px;">
    <div class="partner-badge badge-wide"></div>
    <p class="partner-name" style="margin-top:22px">The Kennel Loft</p>
    <p class="partner-line"><svg viewBox="0 0 12 14"><path d="M6 0a5 5 0 0 0-5 5c0 3.6 5 9 5 9s5-5.4 5-9a5 5 0 0 0-5-5zm0 7a2 2 0 1 1 0-4 2 2 0 0 1 0 4z"/></svg>212 Maple Street</p>
    <p class="partner-line"><svg viewBox="0 0 14 14"><path d="M3 0l3 3-1.6 2a8 8 0 0 0 4.6 4.6L11 8l3 3-2 3C6 14 0 8 0 2z"/></svg>415-555-0178</p>
  </section>

  <section class="partner" style="left:599px; top:848px;">
    <div class="partner-badge badge-round"></div>
    <p class="partner-name">Hillside Pet Supply</p>
    <p class="partner-line"><svg viewBox="0 0 12 14"><path d="M6 0a5 5 0 0 0-5 5c0 3.6 5 9 5 9s5-5.4 5-9a5 5 0 0 0-5-5zm0 7a2 2 0 1 1 0-4 2 2 0 0 1 0 4z"/></svg>1830 Cedar Street</p>
    <p class="partner-line"><svg viewBox="0 0 14 14"><path d="M3 0l3 3-1.6 2a8 8 0 0 0 4.6 4.6L11 8l3 3-2 3C6 14 0 8 0 2z"/></svg>415-555-0193</p>
  </section>

  <section class="partner" style="left:144px; top:1012px;">
    <div class="partner-badge badge-square"></div>
    <p class="partner-name" style="margin-top:14px">Happy Tails Pet Care</p>
    <p class="partner-line"><svg viewBox="0 0 12 14"><path d="M6 0a5 5 0 0 0-5 5c0 3.6 5 9 5 9s5-5.4 5-9a5 5 0 0 0-5-5zm0 7a2 2 0 1 1 0-4 2 2 0 0 1 0 4z"/></svg>340 Seaview Drive, Pacifica</p>
    <p class="partner-line"><svg viewBox="0 0 14 14"><path d="M3 0l3 3-1.6 2a8 8 0 0 0 4.6 4.6L11 8l3 3-2 3C6 14 0 8 0 2z"/></svg>650-555-0126</p>
  </section>

  <section class="partner" style="left:451px; top:1044px;">
    <div class="partner-badge badge-wide" style="background:#1b3a5c; width:230px; height:36px"></div>
    <p class="partner-name" style="margin-top:16px">The Rover Hub</p>
    <p class="partner-line"><svg viewBox="0 0 12 14"><path d="M6 0a5 5 0 0 0-5 5c0 3.6 5 9 5 9s5-5.4 5-9a5 5 0 0 0-5-5zm0 7a2 2 0 1 1 0-4 2 2 0 0 1 0 4z"/></svg>915 Harbor Avenue, Pacifica</p>
    <p class="partner-line"><svg viewBox="0 0 14 14"><path d="M3 0l3 3-1.6 2a8 8 0 0 0 4.6 4.6L11 8l3 3-2 3C6 14 0 8 0 2z"/></svg>650-555-0162</p>
  </section>
</main>
</body>
</html>
```